Label for Fish Food (Aquatic market)

A company based in HK is looking for a new & modern look to refresh our range of fish food for freshwater aquariums. (Original labels attached)
- Range look as we have 5 models & some will be available in 2 sizes.
- Red: Tropical Fish Food (Small Granules) ZP001F (small) & ZP101F (large)
- Blue: Tropical Fish Food (Mini Granules) ZP002F (small) & ZP102F (large)
- Orange: Vemo Nib (Granules) ZP103F (large only)
- Propose a colour: Tropical Fish Food (Pellets) ZP104F (large only)
- Propose a colour: Tropical Fish Food (Stick) ZP105F (large only) (Start with ZP105F as primary project)
- A lot of text in both English & Traditional Chinese, as target market is Hong Kong.
- Bottles & caps are WHITE.
- Label size for 100ml bottles: 132mm (width) x 62mm (height)
- Label size for 250ml bottles: 182mm (width) x 96mm (height)
Updates

Reason: The designs not meet our expectation, we hope we can have more to compare.

Target Market(s)

Hong Kong Aquatic market

Industry/Entity Type

It Company

Font styles to use
Sans Serif

Requirements
Must have
• - Small photo of fish food photo (1:1 scale)
• - ZP logo
• - Made in Europe
• - Room for barcode (no need for batch code, as it is printed on the bottom of the bottle)
• - In fish food packaging, we try to fit photos of 3 to 4 popular types of fish (HK market) into the label, so consumers can relate to their fish easier and purchase our food instead of others. In our original labels, we prefer large image of fish (with parts cut out), if we show the whole fish, then it can be too small. We need Designer input here. (ZP105 Fishes are in a PDF file)
• - Another interesting idea in our range of water treatment, we add fish image with background, so it looks MORE realistic & natural rather than Fish flying mid air on the bottle. But we only selected 1 fish for water treatment, and we want 3 to 4 fish here for fish food.
Nice to have
• Colour codes for different type of fish food, since we will be using the same design for a series of fish food.
Should not have
• Cartoons

```html
<!DOCTYPE html>
<html lang="en">
<head>
<meta charset="utf-8">
<title>ZP Fish Food Label Range</title>
<link href="https://fonts.googleapis.com/css2?family=Roboto:wght@400;700&family=Roboto+Condensed:wght@700&family=Noto+Sans+TC:wght@400;700&display=swap" rel="stylesheet">
<style>
:root{
  --red:#e3262b; --blue:#2a78c2; --orange:#f39a1e; --green:#1e7a3a; --purple:#6a2c91;
  --gold:#e8a100; --ink:#333; --dash:#e98ab8;
  --water-1:#cfe9f7; --water-2:#6fb6e2; --food-1:#b7813f; --food-2:#6e4520;
}
*{box-sizing:border-box;margin:0;padding:0}
html,body{width:1031px;height:1200px;overflow:hidden;background:#fff}
body{position:relative;font-family:"Roboto",sans-serif;color:var(--ink)}
.label{position:absolute;width:452px;height:240px;background:#fff;border:0.8px dashed var(--dash);overflow:hidden;--accent:var(--red);--title:var(--accent)}
.label--red{--accent:var(--red)}
.label--blue{--accent:var(--blue)}
.label--orange{--accent:var(--orange);--title:var(--gold)}
.label--green{--accent:var(--green)}
.label--purple{--accent:var(--purple)}
.spec{position:absolute;left:10px;top:6px;width:112px;font-size:5.2px;line-height:7.4px}
.spec p{margin-bottom:4px}
.spec b{font-weight:700}
.brand{position:absolute;left:143px;top:10px;display:flex;align-items:center;gap:4px}
.brand-square{width:12px;height:12px;background:var(--blue)}
.brand-name{font:700 18px "Roboto",sans-serif;color:var(--blue)}
.origin{position:absolute;left:232px;top:8px;color:var(--accent)}
.origin-en{font-size:8px;font-weight:700}
.origin-cn{font:400 9px "Noto Sans TC",sans-serif;margin-top:2px}
.title{position:absolute;left:140px;top:46px;font:700 23px/26px "Roboto Condensed",sans-serif;color:var(--title);white-space:nowrap;z-index:3}
.model{position:absolute;left:140px;top:72px;font:700 15px/18px "Roboto Condensed",sans-serif;color:var(--title);white-space:nowrap;z-index:3}
.label--orange .title{left:158px}
.label--green .title{top:54px}
.label--green .model{top:80px;left:146px}
.label--purple .model{left:152px}
.scene{position:absolute;left:126px;top:102px;width:212px;height:100px;background:radial-gradient(ellipse at 45% 55%,#fff 0%,var(--water-1) 40%,var(--water-2) 100%)}
.food{position:absolute;left:228px;top:106px;width:58px;height:46px;background:radial-gradient(circle at 40% 40%,var(--food-1),var(--food-2))}
.blurb{position:absolute;left:238px;top:155px;width:94px;font-size:5.2px;line-height:6.8px;z-index:3}
.blurb-cn{font:400 6.8px "Noto Sans TC",sans-serif;line-height:8.4px;margin-top:2px}
.cn{position:absolute;left:332px;top:8px;width:110px;font:400 4.6px "Noto Sans TC",sans-serif;line-height:6.6px}
.cn p{margin-bottom:4px}
.made{position:absolute;left:332px;top:140px;font-size:5px;line-height:7px}
.net{position:absolute;left:383px;top:160px;font-size:8.5px;font-weight:700}
.code-space{position:absolute;left:380px;top:170px;width:58px;height:44px;background:#fff;z-index:2}
.band{position:absolute;left:0;right:0;bottom:0;height:38px;background:var(--accent);color:#fff}
.band-mark{position:absolute;top:8px;left:10px;width:18px;height:18px;border-radius:50%;background:#fff}
.band-badge{position:absolute;top:12px;left:36px;width:30px;height:12px;background:#fff}
.band-seal{position:absolute;top:8px;left:84px;width:24px;height:18px;border-radius:50%;background:#f2c500}
.band-en{position:absolute;left:130px;top:4px;font:700 23px "Roboto",sans-serif}
.band-cn{position:absolute;left:228px;top:4px;font:400 20px "Noto Sans TC",sans-serif}
.band-date{position:absolute;left:350px;bottom:5px;font-size:4.6px}
</style>
</head>
<body>

<section class="label label--red" style="left:49px;top:61px">
  <div class="spec">
    <p><b><i>ZP Tropical</i></b> fish food stick is formulated to provide a balance diet with all necessary nutrients for the growth and development of medium to large size tropical fish. Plus brings out stunning colours of your fish. Our floating sticks contains BETA GLUCAN as a natural immune system booster.</p>
    <p><b>For:</b> Lohan, Siamese tiger fish, all types of large cichlids, Oscar &amp; Arowana etc.</p>
    <p>Feed your fish numerous times a day with enough food that they can consume in about 2-3 minutes. Close the lid properly &amp; store in cool dry place, out of direct sunlight.</p>
    <p><b>Core ingredients:</b> Beta-GLUCAN, vegetable protein concentrates, shells, algae, fish &amp; fish derivatives, cereal, dried yeast, garlic, spirulina, fat, lecithin, antioxidants &amp; EEC permitted colourants</p>
    <p><b>Analysis:</b> protein __%, fat __%, fibre __%, ash __%, moisture __%</p>
    <p><b>Vitamins:</b> A __IU/kg, D3 __IU/kg, E __mg/kg, C __mg/kg</p>
  </div>
  <div class="brand"><span class="brand-square"></span><span class="brand-name">ZP</span></div>
  <div class="origin"><div class="origin-en">100% Made in Europe</div><div class="origin-cn">ZP魚糧 - 歐洲製造</div></div>
  <div class="title">Tropical Fish Food</div>
  <div class="model">ZP001F (Small Granules)</div>
  <div class="scene" role="img" aria-label="Photo of tropical fish swimming in clear water"></div>
  <div class="food" role="img" aria-label="Close-up photo of the fish food granules"></div>
  <div class="blurb">Suitable for all tropical fish. Stunning colours, great health &amp; growth<div class="blurb-cn">適合各種熱帶魚，能帶出亮麗的色彩，促進健康成長。</div></div>
  <div class="cn">
    <p>熱帶魚食糧能為各種中至大型熱帶魚提供均衡及必需的營養，促進魚兒的生長發育，更能令魚兒展現自然艷麗的色彩。</p>
    <p>適合各種中至大型熱帶魚，如花羅漢、泰國虎、鸚鵡、龍魚等。</p>
    <p>一天可多次餵食，份量以魚兒在兩至三分鐘內吃完為適宜。使用後請蓋上蓋子，置於陰涼乾爽處。</p>
    <p>主要成份：葡聚糖、植物蛋白、貝殼、藻類、魚肉、穀物、酵母、大蒜、螺旋藻、脂肪。</p>
    <p>成份分析：蛋白質 __%，脂肪 __%，纖維 __%，灰份 __%，水份 __%</p>
    <p>維他命：維他命A __IU/kg，維他命D3 __IU/kg</p>
  </div>
  <div class="made">Made in Europe for ZP<br>www.zp-aquatics.com<br>Model: ZP105F</div>
  <div class="net">80g / 250ml</div>
  <div class="code-space"></div>
  <div class="band"><span class="band-mark"></span><span class="band-badge"></span><span class="band-seal"></span><span class="band-en">Europe</span><span class="band-cn">歐洲原裝進</span><span class="band-date">Best before: see bottom of container</span></div>
</section>

<section class="label label--red" style="left:538px;top:67px">
  <div class="spec">
    <p><b><i>ZP Tropical</i></b> fish food stick is formulated to provide a balance diet with all necessary nutrients for the growth and development of medium to large size tropical fish. Plus brings out stunning colours of your fish. Our floating sticks contains BETA GLUCAN as a natural immune system booster.</p>
    <p><b>For:</b> Lohan, Siamese tiger fish, all types of large cichlids, Oscar &amp; Arowana etc.</p>
    <p>Feed your fish numerous times a day with enough food that they can consume in about 2-3 minutes. Close the lid properly &amp; store in cool dry place, out of direct sunlight.</p>
    <p><b>Core ingredients:</b> Beta-GLUCAN, vegetable protein concentrates, shells, algae, fish &amp; fish derivatives, cereal, dried yeast, garlic, spirulina, fat, lecithin, antioxidants &amp; EEC permitted colourants</p>
    <p><b>Analysis:</b> protein __%, fat __%, fibre __%, ash __%, moisture __%</p>
    <p><b>Vitamins:</b> A __IU/kg, D3 __IU/kg, E __mg/kg, C __mg/kg</p>
  </div>
  <div class="brand"><span class="brand-square"></span><span class="brand-name">ZP</span></div>
  <div class="origin"><div class="origin-en">100% Made in Europe</div><div class="origin-cn">ZP魚糧 - 歐洲製造</div></div>
  <div class="title">Tropical Fish Food</div>
  <div class="model">ZP101F (Small Granules)</div>
  <div class="scene" role="img" aria-label="Photo of tropical fish swimming in clear water"></div>
  <div class="food" role="img" aria-label="Close-up photo of the fish food granules"></div>
  <div class="blurb">Suitable for all tropical fish. Stunning colours, great health &amp; growth<div class="blurb-cn">適合各種熱帶魚，能帶出亮麗的色彩，促進健康成長。</div></div>
  <div class="cn">
    <p>熱帶魚食糧能為各種中至大型熱帶魚提供均衡及必需的營養，促進魚兒的生長發育，更能令魚兒展現自然艷麗的色彩。</p>
    <p>適合各種中至大型熱帶魚，如花羅漢、泰國虎、鸚鵡、龍魚等。</p>
    <p>一天可多次餵食，份量以魚兒在兩至三分鐘內吃完為適宜。使用後請蓋上蓋子，置於陰涼乾爽處。</p>
    <p>主要成份：葡聚糖、植物蛋白、貝殼、藻類、魚肉、穀物、酵母、大蒜、螺旋藻、脂肪。</p>
    <p>成份分析：蛋白質 __%，脂肪 __%，纖維 __%，灰份 __%，水份 __%</p>
    <p>維他命：維他命A __IU/kg，維他命D3 __IU/kg</p>
  </div>
  <div class="made">Made in Europe for ZP<br>www.zp-aquatics.com<br>Model: ZP105F</div>
  <div class="net">80g / 250ml</div>
  <div class="code-space"></div>
  <div class="band"><span class="band-mark"></span><span class="band-badge"></span><span class="band-seal"></span><span class="band-en">Europe</span><span class="band-cn">歐洲原裝進</span><span class="band-date">Best before: see bottom of container</span></div>
</section>

<section class="label label--blue" style="left:49px;top:327px">
  <div class="spec">
    <p><b><i>ZP Tropical</i></b> fish food stick is formulated to provide a balance diet with all necessary nutrients for the growth and development of medium to large size tropical fish. Plus brings out stunning colours of your fish. Our floating sticks contains BETA GLUCAN as a natural immune system booster.</p>
    <p><b>For:</b> Lohan, Siamese tiger fish, all types of large cichlids, Oscar &amp; Arowana etc.</p>
    <p>Feed your fish numerous times a day with enough food that they can consume in about 2-3 minutes. Close the lid properly &amp; store in cool dry place, out of direct sunlight.</p>
    <p><b>Core ingredients:</b> Beta-GLUCAN, vegetable protein concentrates, shells, algae, fish &amp; fish derivatives, cereal, dried yeast, garlic, spirulina, fat, lecithin, antioxidants &amp; EEC permitted colourants</p>
    <p><b>Analysis:</b> protein __%, fat __%, fibre __%, ash __%, moisture __%</p>
    <p><b>Vitamins:</b> A __IU/kg, D3 __IU/kg, E __mg/kg, C __mg/kg</p>
  </div>
  <div class="brand"><span class="brand-square"></span><span class="brand-name">ZP</span></div>
  <div class="origin"><div class="origin-en">100% Made in Europe</div><div class="origin-cn">ZP魚糧 - 歐洲製造</div></div>
  <div class="title">Tropical Fish Food</div>
  <div class="model">ZP002F (Mini Granules)</div>
  <div class="scene" role="img" aria-label="Photo of tropical fish swimming in clear water"></div>
  <div class="food" role="img" aria-label="Close-up photo of the fish food granules"></div>
  <div class="blurb">Suitable for all tropical fish. Stunning colours, great health &amp; growth<div class="blurb-cn">適合各種熱帶魚，能帶出亮麗的色彩，促進健康成長。</div></div>
  <div class="cn">
    <p>熱帶魚食糧能為各種中至大型熱帶魚提供均衡及必需的營養，促進魚兒的生長發育，更能令魚兒展現自然艷麗的色彩。</p>
    <p>適合各種中至大型熱帶魚，如花羅漢、泰國虎、鸚鵡、龍魚等。</p>
    <p>一天可多次餵食，份量以魚兒在兩至三分鐘內吃完為適宜。使用後請蓋上蓋子，置於陰涼乾爽處。</p>
    <p>主要成份：葡聚糖、植物蛋白、貝殼、藻類、魚肉、穀物、酵母、大蒜、螺旋藻、脂肪。</p>
    <p>成份分析：蛋白質 __%，脂肪 __%，纖維 __%，灰份 __%，水份 __%</p>
    <p>維他命：維他命A __IU/kg，維他命D3 __IU/kg</p>
  </div>
  <div class="made">Made in Europe for ZP<br>www.zp-aquatics.com<br>Model: ZP105F</div>
  <div class="net">80g / 250ml</div>
  <div class="code-space"></div>
  <div class="band"><span class="band-mark"></span><span class="band-badge"></span><span class="band-seal"></span><span class="band-en">Europe</span><span class="band-cn">歐洲原裝進</span><span class="band-date">Best before: see bottom of container</span></div>
</section>

<section class="label label--blue" style="left:538px;top:333px">
  <div class="spec">
    <p><b><i>ZP Tropical</i></b> fish food stick is formulated to provide a balance diet with all necessary nutrients for the growth and development of medium to large size tropical fish. Plus brings out stunning colours of your fish. Our floating sticks contains BETA GLUCAN as a natural immune system booster.</p>
    <p><b>For:</b> Lohan, Siamese tiger fish, all types of large cichlids, Oscar &amp; Arowana etc.</p>
    <p>Feed your fish numerous times a day with enough food that they can consume in about 2-3 minutes. Close the lid properly &amp; store in cool dry place, out of direct sunlight.</p>
    <p><b>Core ingredients:</b> Beta-GLUCAN, vegetable protein concentrates, shells, algae, fish &amp; fish derivatives, cereal, dried yeast, garlic, spirulina, fat, lecithin, antioxidants &amp; EEC permitted colourants</p>
    <p><b>Analysis:</b> protein __%, fat __%, fibre __%, ash __%, moisture __%</p>
    <p><b>Vitamins:</b> A __IU/kg, D3 __IU/kg, E __mg/kg, C __mg/kg</p>
  </div>
  <div class="brand"><span class="brand-square"></span><span class="brand-name">ZP</span></div>
  <div class="origin"><div class="origin-en">100% Made in Europe</div><div class="origin-cn">ZP魚糧 - 歐洲製造</div></div>
  <div class="title">Tropical Fish Food</div>
  <div class="model">ZP102F (Mini Granules)</div>
  <div class="scene" role="img" aria-label="Photo of tropical fish swimming in clear water"></div>
  <div class="food" role="img" aria-label="Close-up photo of the fish food granules"></div>
  <div class="blurb">Suitable for all tropical fish. Stunning colours, great health &amp; growth<div class="blurb-cn">適合各種熱帶魚，能帶出亮麗的色彩，促進健康成長。</div></div>
  <div class="cn">
    <p>熱帶魚食糧能為各種中至大型熱帶魚提供均衡及必需的營養，促進魚兒的生長發育，更能令魚兒展現自然艷麗的色彩。</p>
    <p>適合各種中至大型熱帶魚，如花羅漢、泰國虎、鸚鵡、龍魚等。</p>
    <p>一天可多次餵食，份量以魚兒在兩至三分鐘內吃完為適宜。使用後請蓋上蓋子，置於陰涼乾爽處。</p>
    <p>主要成份：葡聚糖、植物蛋白、貝殼、藻類、魚肉、穀物、酵母、大蒜、螺旋藻、脂肪。</p>
    <p>成份分析：蛋白質 __%，脂肪 __%，纖維 __%，灰份 __%，水份 __%</p>
    <p>維他命：維他命A __IU/kg，維他命D3 __IU/kg</p>
  </div>
  <div class="made">Made in Europe for ZP<br>www.zp-aquatics.com<br>Model: ZP105F</div>
  <div class="net">80g / 250ml</div>
  <div class="code-space"></div>
  <div class="band"><span class="band-mark"></span><span class="band-badge"></span><span class="band-seal"></span><span class="band-en">Europe</span><span class="band-cn">歐洲原裝進</span><span class="band-date">Best before: see bottom of container</span></div>
</section>

<section class="label label--orange" style="left:45px;top:611px">
  <div class="spec">
    <p><b><i>ZP Tropical</i></b> fish food stick is formulated to provide a balance diet with all necessary nutrients for the growth and development of medium to large size tropical fish. Plus brings out stunning colours of your fish. Our floating sticks contains BETA GLUCAN as a natural immune system booster.</p>
    <p><b>For:</b> Lohan, Siamese tiger fish, all types of large cichlids, Oscar &amp; Arowana etc.</p>
    <p>Feed your fish numerous times a day with enough food that they can consume in about 2-3 minutes. Close the lid properly &amp; store in cool dry place, out of direct sunlight.</p>
    <p><b>Core ingredients:</b> Beta-GLUCAN, vegetable protein concentrates, shells, algae, fish &amp; fish derivatives, cereal, dried yeast, garlic, spirulina, fat, lecithin, antioxidants &amp; EEC permitted colourants</p>
    <p><b>Analysis:</b> protein __%, fat __%, fibre __%, ash __%, moisture __%</p>
    <p><b>Vitamins:</b> A __IU/kg, D3 __IU/kg, E __mg/kg, C __mg/kg</p>
  </div>
  <div class="brand"><span class="brand-square"></span><span class="brand-name">ZP</span></div>
  <div class="origin"><div class="origin-en">100% Made in Europe</div><div class="origin-cn">ZP魚糧 - 歐洲製造</div></div>
  <div class="title">Vemo Nib</div>
  <div class="model">ZP103F (Granules)</div>
  <div class="scene" role="img" aria-label="Photo of tropical fish swimming in clear water"></div>
  <div class="food" role="img" aria-label="Close-up photo of the fish food granules"></div>
  <div class="blurb">Suitable for all tropical fish. Stunning colours, great health &amp; growth<div class="blurb-cn">適合各種熱帶魚，能帶出亮麗的色彩，促進健康成長。</div></div>
  <div class="cn">
    <p>熱帶魚食糧能為各種中至大型熱帶魚提供均衡及必需的營養，促進魚兒的生長發育，更能令魚兒展現自然艷麗的色彩。</p>
    <p>適合各種中至大型熱帶魚，如花羅漢、泰國虎、鸚鵡、龍魚等。</p>
    <p>一天可多次餵食，份量以魚兒在兩至三分鐘內吃完為適宜。使用後請蓋上蓋子，置於陰涼乾爽處。</p>
    <p>主要成份：葡聚糖、植物蛋白、貝殼、藻類、魚肉、穀物、酵母、大蒜、螺旋藻、脂肪。</p>
    <p>成份分析：蛋白質 __%，脂肪 __%，纖維 __%，灰份 __%，水份 __%</p>
    <p>維他命：維他命A __IU/kg，維他命D3 __IU/kg</p>
  </div>
  <div class="made">Made in Europe for ZP<br>www.zp-aquatics.com<br>Model: ZP105F</div>
  <div class="net">80g / 250ml</div>
  <div class="code-space"></div>
  <div class="band"><span class="band-mark"></span><span class="band-badge"></span><span class="band-seal"></span><span class="band-en">Europe</span><span class="band-cn">歐洲原裝進</span><span class="band-date">Best before: see bottom of container</span></div>
</section>

<section class="label label--green" style="left:522px;top:612px">
  <div class="spec">
    <p><b><i>ZP Tropical</i></b> fish food stick is formulated to provide a balance diet with all necessary nutrients for the growth and development of medium to large size tropical fish. Plus brings out stunning colours of your fish. Our floating sticks contains BETA GLUCAN as a natural immune system booster.</p>
    <p><b>For:</b> Lohan, Siamese tiger fish, all types of large cichlids, Oscar &amp; Arowana etc.</p>
    <p>Feed your fish numerous times a day with enough food that they can consume in about 2-3 minutes. Close the lid properly &amp; store in cool dry place, out of direct sunlight.</p>
    <p><b>Core ingredients:</b> Beta-GLUCAN, vegetable protein concentrates, shells, algae, fish &amp; fish derivatives, cereal, dried yeast, garlic, spirulina, fat, lecithin, antioxidants &amp; EEC permitted colourants</p>
    <p><b>Analysis:</b> protein __%, fat __%, fibre __%, ash __%, moisture __%</p>
    <p><b>Vitamins:</b> A __IU/kg, D3 __IU/kg, E __mg/kg, C __mg/kg</p>
  </div>
  <div class="brand"><span class="brand-square"></span><span class="brand-name">ZP</span></div>
  <div class="origin"><div class="origin-en">100% Made in Europe</div><div class="origin-cn">ZP魚糧 - 歐洲製造</div></div>
  <div class="title">Tropical Fish Food</div>
  <div class="model">ZP105F (Stick)</div>
  <div class="scene" role="img" aria-label="Photo of tropical fish swimming in clear water"></div>
  <div class="food" role="img" aria-label="Close-up photo of the fish food sticks"></div>
  <div class="blurb">Suitable for all tropical fish. Stunning colours, great health &amp; growth<div class="blurb-cn">適合各種熱帶魚，能帶出亮麗的色彩，促進健康成長。</div></div>
  <div class="cn">
    <p>熱帶魚食糧能為各種中至大型熱帶魚提供均衡及必需的營養，促進魚兒的生長發育，更能令魚兒展現自然艷麗的色彩。</p>
    <p>適合各種中至大型熱帶魚，如花羅漢、泰國虎、鸚鵡、龍魚等。</p>
    <p>一天可多次餵食，份量以魚兒在兩至三分鐘內吃完為適宜。使用後請蓋上蓋子，置於陰涼乾爽處。</p>
    <p>主要成份：葡聚糖、植物蛋白、貝殼、藻類、魚肉、穀物、酵母、大蒜、螺旋藻、脂肪。</p>
    <p>成份分析：蛋白質 __%，脂肪 __%，纖維 __%，灰份 __%，水份 __%</p>
    <p>維他命：維他命A __IU/kg，維他命D3 __IU/kg</p>
  </div>
  <div class="made">Made in Europe for ZP<br>www.zp-aquatics.com<br>Model: ZP105F</div>
  <div class="net">80g / 250ml</div>
  <div class="code-space"></div>
  <div class="band"><span class="band-mark"></span><span class="band-badge"></span><span class="band-seal"></span><span class="band-en">Europe</span><span class="band-cn">歐洲原裝進</span><span class="band-date">Best before: see bottom of container</span></div>
</section>

<section class="label label--purple" style="left:42px;top:882px">
  <div class="spec">
    <p><b><i>ZP Tropical</i></b> fish food stick is formulated to provide a balance diet with all necessary nutrients for the growth and development of medium to large size tropical fish. Plus brings out stunning colours of your fish. Our floating sticks contains BETA GLUCAN as a natural immune system booster.</p>
    <p><b>For:</b> Lohan, Siamese tiger fish, all types of large cichlids, Oscar &amp; Arowana etc.</p>
    <p>Feed your fish numerous times a day with enough food that they can consume in about 2-3 minutes. Close the lid properly &amp; store in cool dry place, out of direct sunlight.</p>
    <p><b>Core ingredients:</b> Beta-GLUCAN, vegetable protein concentrates, shells, algae, fish &amp; fish derivatives, cereal, dried yeast, garlic, spirulina, fat, lecithin, antioxidants &amp; EEC permitted colourants</p>
    <p><b>Analysis:</b> protein __%, fat __%, fibre __%, ash __%, moisture __%</p>
    <p><b>Vitamins:</b> A __IU/kg, D3 __IU/kg, E __mg/kg, C __mg/kg</p>
  </div>
  <div class="brand"><span class="brand-square"></span><span class="brand-name">ZP</span></div>
  <div class="origin"><div class="origin-en">100% Made in Europe</div><div class="origin-cn">ZP魚糧 - 歐洲製造</div></div>
  <div class="title">Tropical Fish Food</div>
  <div class="model">ZP104F (Pellets)</div>
  <div class="scene" role="img" aria-label="Photo of tropical fish swimming in clear water"></div>
  <div class="food" role="img" aria-label="Close-up photo of the fish food pellets"></div>
  <div class="blurb">Suitable for all tropical fish. Stunning colours, great health &amp; growth<div class="blurb-cn">適合各種熱帶魚，能帶出亮麗的色彩，促進健康成長。</div></div>
  <div class="cn">
    <p>熱帶魚食糧能為各種中至大型熱帶魚提供均衡及必需的營養，促進魚兒的生長發育，更能令魚兒展現自然艷麗的色彩。</p>
    <p>適合各種中至大型熱帶魚，如花羅漢、泰國虎、鸚鵡、龍魚等。</p>
    <p>一天可多次餵食，份量以魚兒在兩至三分鐘內吃完為適宜。使用後請蓋上蓋子，置於陰涼乾爽處。</p>
    <p>主要成份：葡聚糖、植物蛋白、貝殼、藻類、魚肉、穀物、酵母、大蒜、螺旋藻、脂肪。</p>
    <p>成份分析：蛋白質 __%，脂肪 __%，纖維 __%，灰份 __%，水份 __%</p>
    <p>維他命：維他命A __IU/kg，維他命D3 __IU/kg</p>
  </div>
  <div class="made">Made in Europe for ZP<br>www.zp-aquatics.com<br>Model: ZP105F</div>
  <div class="net">80g / 250ml</div>
  <div class="code-space"></div>
  <div class="band"><span class="band-mark"></span><span class="band-badge"></span><span class="band-seal"></span><span class="band-en">Europe</span><span class="band-cn">歐洲原裝進</span><span class="band-date">Best before: see bottom of container</span></div>
</section>

</body>
</html>
```